Business Card Design

We offer Procurement, Supply Chain, Merchandise Expediting, Customs Management, Shipping Documentation and many other Specialized Consultancies. The many products we handle are used in many different industries like Oil, Gas and Drilling Hardware, Construction Equipment, Industrial Parts and much more.
Our Slogan is:
"We look from around the world for what you need, bringing it to your door in the shortest possible time with the best all inclusive price"

Target Market(s)

US Export companies, Mexican Import companies and others companies that are looking for Oil & Gas products

Industry/Entity Type

Business

Contact Information for Business Card

Corvinet Trade Partners & Providers, LLC
Phone: +1 (281) 555-0193
31542 Larkfield Pkwy, Ste 1800
Katy, Texas 77000 USA
www.corvinet.biz

Font styles to use
Other font styles liked:
• Century Gothic

```html
<!DOCTYPE html>
<html lang="en">
<head>
<meta charset="utf-8">
<title>Corvinet Trade Partners &amp; Providers – Business Card</title>
<link rel="stylesheet" href="https://fonts.googleapis.com/css2?family=Questrial&display=swap">
<style>
  :root {
    --brand-red: #e83a4a;
    --brand-green: #0e7a45;
    --ink: #3a3a3a;
    --card: #ffffff;
    --stage: #8b6a47;
    --mark-faint: #fcecee;
  }
  * { box-sizing: border-box; margin: 0; padding: 0; }
  html, body {
    width: 1018px; height: 1200px; overflow: hidden;
    background: var(--stage);
    font-family: "Questrial", "Century Gothic", sans-serif;
  }
  .canvas { position: relative; width: 1018px; height: 1200px; }
  .card {
    position: absolute; left: 99px; width: 820px; height: 470px;
    background: var(--card);
    box-shadow: 0 4px 14px rgba(0,0,0,.25);
    overflow: hidden;
  }
  .card--front { top: 110px; }
  .card--back { top: 620px; display: flex; align-items: center; justify-content: center; }

  .card__watermark {
    position: absolute; left: 257px; top: 72px; width: 306px; height: 306px;
    background: var(--mark-faint); border-radius: 34px;
  }
  .brand { position: absolute; left: 124px; top: 40px; width: 578px; }
  .brand__row { display: flex; align-items: flex-end; gap: 14px; }
  .brand__square {
    width: 104px; height: 104px; background: var(--brand-red); border-radius: 12px; flex: none;
  }
  .brand__name {
    color: var(--brand-green); font-size: 112px; line-height: .8;
    letter-spacing: -2px; font-weight: 400;
  }
  .brand__rule { height: 4px; background: var(--brand-red); margin-top: 4px; }
  .brand__tagline {
    color: var(--brand-red); font-size: 35px; text-align: right; margin-top: 4px; letter-spacing: -.3px;
  }

  .contact {
    position: absolute; left: 0; right: 0; top: 308px;
    display: flex; flex-direction: column; align-items: center; gap: 20px;
    color: var(--ink); font-size: 22px;
  }
  .contact__line { display: flex; align-items: center; gap: 8px; line-height: 26px; }
  .contact__icon { width: 22px; height: 22px; fill: var(--brand-red); flex: none; }

  .back__mark { width: 297px; height: 297px; background: var(--brand-red); border-radius: 26px; }
</style>
</head>
<body>
<main class="canvas">
  <section class="card card--front" aria-label="Business card front">
    <div class="card__watermark" aria-hidden="true"></div>
    <div class="brand">
      <div class="brand__row">
        <div class="brand__square" aria-hidden="true"></div>
        <span class="brand__name">corvinet</span>
      </div>
      <div class="brand__rule"></div>
      <p class="brand__tagline">trade partners &amp; providers, llc</p>
    </div>
    <div class="contact">
      <p class="contact__line">
        <svg class="contact__icon" viewBox="0 0 24 24" aria-hidden="true"><path d="M7 2h3l1 5-2.5 1.5c1 2.5 3 4.5 5.5 5.5L15.5 11.5 21 13v3c0 2-1.5 3.5-3.5 3.5C10 19 4.5 13.5 4 6 4 4 5 2 7 2z"/></svg>
        +1 (281) 555-0193 31542
      </p>
      <p class="contact__line">
        <svg class="contact__icon" viewBox="0 0 24 24" aria-hidden="true"><path d="M12 2a10 10 0 1 0 0 20 10 10 0 0 0 0-20zm0 2c.9 1 1.7 2.6 2.1 5H9.9C10.3 6.6 11.1 5 12 4zM4.3 11h3.5c.1-2.3.6-4.2 1.4-5.6A8 8 0 0 0 4.3 11zm0 2a8 8 0 0 0 4.9 5.6c-.8-1.4-1.3-3.3-1.4-5.6H4.3zm5.6 0c.4 2.4 1.2 4 2.1 5 .9-1 1.7-2.6 2.1-5H9.9zm6.3 0c-.1 2.3-.6 4.2-1.4 5.6a8 8 0 0 0 4.9-5.6h-3.5zm3.5-2a8 8 0 0 0-4.9-5.6c.8 1.4 1.3 3.3 1.4 5.6h3.5z"/></svg>
        www.corvinet.biz
      </p>
      <p class="contact__line">
        <svg class="contact__icon" viewBox="0 0 24 24" aria-hidden="true"><path d="M12 3 2 12h3v8h5v-5h4v5h5v-8h3z"/></svg>
        Larkfield Pkwy, Ste 1800 Katy, Texas 77000 USA
      </p>
    </div>
  </section>

  <section class="card card--back" aria-label="Business card back">
    <div class="back__mark" aria-hidden="true"></div>
  </section>
</main>
</body>
</html>
```